Roofing & Siding door hanger flyer

-Looking to make door hanger flyer for Pellmont Roofing & Siding
-4.5" wide x 11" tall
-2 sided full colour
-We have started a new website (the content is changing) I have attached photos.
-About us:
-25 year labour warranty's available
-32 years in Calgary
-QCR A+ Member
-NWTG (Prairie Joint Shingle Guild) (logo attached)
-KOV Summit Select (logo attached)
-Owen Brisket (logo attached)
-Slogan "Raised On Care, Proven Through Seasons" 32 years in Calgary
-Sale
-Page 1 & 2 design ideas
We are in your area, contact us today for your Exclusive limited time offer! *discounts apply exclusively to new agreements only
Updates
-Please keep simple, clean & bright
-I really like the bright blue from our new logo (new logo uploaded)
-We specialize in Roofing -Siding-Gutters & full Exterior Renos (like the competitor example uploaded)
-This is the NEW website we are currently working on (not finished) https://mockview.example-draftpad.net/view/1a2b3c4d-5e6f-4a7b-8c9d-0e1f2a3b4c5d-7k2m/?fullscreen
-This is our OLD website https://pellmontshingleworks.com
-For the sale "We are in your area, contact us today for your Exclusive limited time offer" *discounts apply exclusively to new agreements only
-Free Estimates
-our phone# is 403-555-0148
-our website is pellmontshingleworks.com
-keep simple, clean, bright use the "new logo" uploaded. Check out the competitor example uploaded file
-We are in your area, Contact us today for your Exclusive limited time offer! *discounts apply to new agreements only
-FREE ESTIMATES
-Specialized in Roofing /Siding /Gutters Full Exterior Reno's
-We are currently working on a NEW website https://mockview.example-draftpad.net/view/1a2b3c4d-5e6f-4a7b-8c9d-0e1f2a3b4c5d-7k2m/?fullscreen
-Our OLD website https://pellmontshingleworks.com/
-Post old site address on flyer pellmontshingleworks.com
-Phone # 403-555-0148
Target Market(s)
40-55
Industry/Entity Type
Roofing Siding & full Exterior Reno's
Look and feel

```html
<!DOCTYPE html>
<html lang="en">
<head>
<meta charset="utf-8">
<title>Pellmont Roofing &amp; Siding – Door Hanger</title>
<link rel="stylesheet" href="https://fonts.googleapis.com/css2?family=Montserrat:wght@500;600;700;800&display=swap">
<style>
  :root {
    --bg: #e6e6e6;
    --blue: #1a7fe0;
    --blue-deep: #0b5fc6;
    --blue-box: #1668cf;
    --red: #e31b1b;
    --ink: #1d1d1d;
    --white: #ffffff;
  }
  * { margin: 0; padding: 0; box-sizing: border-box; }
  html, body { width: 1200px; height: 2257px; overflow: hidden; background: var(--bg); }
  body { position: relative; font-family: "Montserrat", sans-serif; }

  .hanger {
    position: absolute;
    width: 440px; height: 1075px;
    background: var(--white);
    overflow: hidden;
    transform: scale(0.876);
    transform-origin: 0 0;
  }
  .hanger--front-top { left: 145px; top: 83px; }
  .hanger--back-top  { left: 643px; top: 83px; }
  .hanger--front-cut { left: 145px; top: 1194px; border-top-left-radius: 48px; }
  .hanger--back-cut  { left: 643px; top: 1194px; border-top-left-radius: 48px; }

  .abs { position: absolute; }

  .photo-house {
    left: 0; top: 0; width: 440px; height: 490px;
    background: linear-gradient(180deg, #6fb1f0 0%, #a9cff3 28%, #8d9aa6 45%, #cfc7b8 70%, #9aa3ab 100%);
  }
  .photo-estate {
    left: 0; top: 0; width: 440px; height: 450px;
    background: linear-gradient(180deg, #7d8fa0 0%, #c7cfd8 35%, #e4e3dc 55%, #5f7a4a 85%, #48633a 100%);
  }

  .swoop { left: 0; width: 440px; height: 130px; }

  .tagline { right: 15px; top: 20px; text-align: right; font-weight: 700; }
  .tagline__small { font-size: 16px; color: var(--blue-deep); letter-spacing: .3px; }
  .tagline__big { font-size: 26px; color: var(--blue); line-height: 1.15; }

  .badge-ring {
    left: 75px; top: 320px; width: 290px; height: 290px; border-radius: 50%;
    background: rgba(255,255,255,.55);
  }
  .badge-core {
    left: 95px; top: 340px; width: 250px; height: 250px; border-radius: 50%;
    background: var(--white);
  }
  .brand { left: 0; width: 440px; top: 432px; text-align: center; color: var(--ink); font-weight: 600; }
  .brand__name { font-size: 40px; letter-spacing: 3px; line-height: 1.1; }
  .brand__trade { font-size: 17px; letter-spacing: 4px; margin-top: 6px; }

  .heading { font-weight: 700; line-height: 1; }
  .heading--blue { color: var(--blue); font-size: 32px; }
  .heading--red  { color: var(--red);  font-size: 32px; }

  .item { font-weight: 600; color: var(--blue-deep); white-space: nowrap; }
  .item--lg { font-size: 21px; }
  .item--md { font-size: 19px; }
  .item--ink { font-weight: 500; color: var(--ink); font-size: 16px; }

  .band { left: 0; bottom: 0; width: 440px; height: 78px; background: var(--blue); }
  .phone-box {
    background: var(--blue-box); border: 3px solid var(--white); border-radius: 10px;
    color: var(--white); font-weight: 700; text-align: center;
  }
  .phone-box--front { left: 35px; top: 968px; width: 372px; height: 62px; font-size: 40px; line-height: 56px; }
  .phone-box--back  { left: 74px; top: 983px; width: 290px; height: 46px; font-size: 29px; line-height: 40px; }
  .site { left: 0; width: 440px; top: 1036px; text-align: center; color: var(--white); font-size: 21px; font-weight: 600; letter-spacing: 1.6px; }

  .worker-photo {
    left: 86px; top: 330px; width: 268px; height: 268px; border-radius: 50%;
    background: radial-gradient(circle at 40% 45%, #c89a7a 0%, #4e7fc7 35%, #6f6a5e 70%, #3d3a35 100%);
    border: 8px solid rgba(255,255,255,.7);
  }

  .slogan { left: 0; width: 440px; top: 609px; text-align: center; font-weight: 700; color: var(--blue); font-size: 26px; line-height: 34px; }
  .years { left: 0; width: 440px; top: 678px; text-align: center; font-weight: 700; color: var(--red); font-size: 29px; }
  .offer { left: 27px; width: 400px; top: 725px; font-size: 14px; font-weight: 500; color: var(--ink); line-height: 1.2; }
  .fine  { left: 27px; top: 774px; font-size: 13.5px; font-weight: 500; color: var(--ink); }
  .estimates { left: 27px; top: 800px; font-size: 33px; font-weight: 700; color: var(--blue); }
  .specialized { left: 27px; top: 843px; font-size: 18px; font-weight: 700; color: var(--red); text-decoration: underline; }
  .spec-item { font-size: 16.5px; font-weight: 600; color: var(--blue-deep); line-height: 24px; }

  .partners { left: 27px; top: 937px; width: 390px; height: 40px; display: flex; justify-content: space-between; align-items: center; }
  .partner { width: 38px; height: 34px; background: #c9d6e6; }
  .partner--round { border-radius: 50%; background: #c9a640; width: 36px; height: 36px; }
  .partner--square { background: #d8dee6; }
  .partner--red { background: #d9302b; }
  .partner--navy { background: #1f3f86; transform: rotate(45deg); width: 28px; height: 28px; }
  .partner--green { border-radius: 50%; background: #6aa84f; width: 26px; height: 26px; }

  .hang-hole { fill: var(--white); }
</style>
</head>
<body>

<section class="hanger hanger--front-top">
  <div class="abs photo-house" role="img" aria-label="Photo of a stone house with a new grey shingle roof under blue sky"></div>
  <svg class="abs swoop" style="top:400px" viewBox="0 0 440 130" aria-hidden="true">
    <path d="M0 30 Q110 105 220 100 Q330 105 440 30 V62 Q330 128 220 126 Q110 128 0 62Z" fill="var(--blue)"/>
    <path d="M0 62 Q110 128 220 126 Q330 128 440 62 V130 H0Z" fill="var(--white)"/>
  </svg>
  <div class="abs tagline"><div class="tagline__small">WE'RE IN YOUR</div><div class="tagline__big">NEIGHBOURHOOD!</div></div>
  <div class="abs badge-ring"></div>
  <div class="abs badge-core"></div>
  <div class="abs brand"><div class="brand__name">PELLMONT</div><div class="brand__trade">ROOFING &amp; SIDING</div></div>

  <h2 class="abs heading heading--blue" style="left:15px;top:537px">ROOFING</h2>
  <span class="abs item item--lg" style="left:15px;top:585px">• Asphalt</span>
  <span class="abs item item--lg" style="left:160px;top:585px">• Rubber</span>
  <span class="abs item item--lg" style="left:307px;top:585px">• Metal</span>

  <h2 class="abs heading heading--blue" style="left:15px;top:656px">SIDING</h2>
  <span class="abs item item--md" style="left:15px;top:705px">• Brisket fibre cement</span>
  <span class="abs item item--md" style="left:15px;top:734px">• Metal(steel, Aluminum)</span>
  <span class="abs item item--md" style="left:307px;top:705px">• Vinyl</span>
  <span class="abs item item--md" style="left:307px;top:734px">• Plankline</span>

  <h2 class="abs heading heading--red" style="left:15px;top:792px">FULL EXTERIORS</h2>
  <span class="abs item item--ink" style="left:15px;top:836px">• Eavestrough /soffit/ Fascia</span>
  <span class="abs item item--ink" style="left:15px;top:869px">• Stone</span>
  <span class="abs item item--ink" style="left:15px;top:901px">• Insulation Windows &amp; Doors</span>
  <span class="abs item item--ink" style="left:15px;top:934px">• Shake Repairs</span>
  <span class="abs item item--ink" style="left:307px;top:836px">• Stucco</span>
  <span class="abs item item--ink" style="left:307px;top:869px">• Skylights</span>
  <span class="abs item item--ink" style="left:307px;top:901px">• Painting</span>

  <div class="abs band"></div>
  <div class="abs phone-box phone-box--front">(403) 555-0148</div>
  <div class="abs site">www.pellmontshingleworks.com</div>
</section>

<section class="hanger hanger--back-top">
  <div class="abs photo-estate" role="img" aria-label="Photo of a large white estate house with a blue metal roof and lawn"></div>
  <svg class="abs swoop" style="top:370px" viewBox="0 0 440 130" aria-hidden="true">
    <path d="M0 40 Q110 105 220 100 Q330 105 440 40 V70 Q330 128 220 126 Q110 128 0 70Z" fill="var(--blue)"/>
    <path d="M0 70 Q110 128 220 126 Q330 128 440 70 V130 H0Z" fill="var(--white)"/>
  </svg>
  <div class="abs tagline"><div class="tagline__small">WE'RE IN YOUR</div><div class="tagline__big">NEIGHBOURHOOD!</div></div>
  <div class="abs worker-photo" role="img" aria-label="Photo of a roofer in a blue cap cleaning a gutter"></div>

  <div class="abs slogan">Raised On Care,<br>Proven Through Seasons</div>
  <div class="abs years">32 YEARS IN CALGARY</div>
  <p class="abs offer">We are in your area, contact us today for your Exclusive limited time offer</p>
  <p class="abs fine">*Discounts apply exclusively to new agreements only</p>
  <h2 class="abs estimates">FREE ESTIMATES</h2>
  <div class="abs specialized">SPECIALIZED IN</div>
  <div class="abs spec-item" style="left:35px;top:876px">• Gutters Full<br>&nbsp;&nbsp;&nbsp;Exterior Reno's</div>
  <div class="abs spec-item" style="left:262px;top:876px">• Roofing<br>• Siding</div>
  <div class="abs partners">
    <span class="partner partner--square"></span>
    <span class="partner"></span>
    <span class="partner partner--red"></span>
    <span class="partner partner--round"></span>
    <span class="partner partner--navy"></span>
    <span class="partner partner--green"></span>
  </div>

  <div class="abs band"></div>
  <div class="abs phone-box phone-box--back">(403) 555-0148</div>
  <div class="abs site">www.pellmontshingleworks.com</div>
</section>

<section class="hanger hanger--front-cut">
  <div class="abs photo-house" role="img" aria-label="Photo of a stone house with a new grey shingle roof under blue sky"></div>
  <svg class="abs swoop" style="top:400px" viewBox="0 0 440 130" aria-hidden="true">
    <path d="M0 30 Q110 105 220 100 Q330 105 440 30 V62 Q330 128 220 126 Q110 128 0 62Z" fill="var(--blue)"/>
    <path d="M0 62 Q110 128 220 126 Q330 128 440 62 V130 H0Z" fill="var(--white)"/>
  </svg>
  <div class="abs tagline"><div class="tagline__small">WE'RE IN YOUR</div><div class="tagline__big">NEIGHBOURHOOD!</div></div>
  <svg class="abs" style="left:0;top:0" width="440" height="260" viewBox="0 0 440 260" aria-hidden="true">
    <path class="hang-hole" d="M0 130 H130 Q145 130 155 120 A72 72 0 1 1 155 200 Q145 190 130 190 H0Z"/>
  </svg>
  <div class="abs badge-ring"></div>
  <div class="abs badge-core"></div>
  <div class="abs brand"><div class="brand__name">PELLMONT</div><div class="brand__trade">ROOFING &amp; SIDING</div></div>

  <h2 class="abs heading heading--blue" style="left:15px;top:537px">ROOFING</h2>
  <span class="abs item item--lg" style="left:15px;top:585px">• Asphalt</span>
  <span class="abs item item--lg" style="left:160px;top:585px">• Rubber</span>
  <span class="abs item item--lg" style="left:307px;top:585px">• Metal</span>

  <h2 class="abs heading heading--blue" style="left:15px;top:656px">SIDING</h2>
  <span class="abs item item--md" style="left:15px;top:705px">• Brisket fibre cement</span>
  <span class="abs item item--md" style="left:15px;top:734px">• Metal(steel, Aluminum)</span>
  <span class="abs item item--md" style="left:307px;top:705px">• Vinyl</span>
  <span class="abs item item--md" style="left:307px;top:734px">• Plankline</span>

  <h2 class="abs heading heading--red" style="left:15px;top:792px">FULL EXTERIORS</h2>
  <span class="abs item item--ink" style="left:15px;top:836px">• Eavestrough /soffit/ Fascia</span>
  <span class="abs item item--ink" style="left:15px;top:869px">• Stone</span>
  <span class="abs item item--ink" style="left:15px;top:901px">• Insulation Windows &amp; Doors</span>
  <span class="abs item item--ink" style="left:15px;top:934px">• Shake Repairs</span>
  <span class="abs item item--ink" style="left:307px;top:836px">• Stucco</span>
  <span class="abs item item--ink" style="left:307px;top:869px">• Skylights</span>
  <span class="abs item item--ink" style="left:307px;top:901px">• Painting</span>

  <div class="abs band"></div>
  <div class="abs phone-box phone-box--front">(403) 555-0148</div>
  <div class="abs site">www.pellmontshingleworks.com</div>
</section>

<section class="hanger hanger--back-cut">
  <div class="abs photo-estate" role="img" aria-label="Photo of a large white estate house with a blue metal roof and lawn"></div>
  <svg class="abs swoop" style="top:370px" viewBox="0 0 440 130" aria-hidden="true">
    <path d="M0 40 Q110 105 220 100 Q330 105 440 40 V70 Q330 128 220 126 Q110 128 0 70Z" fill="var(--blue)"/>
    <path d="M0 70 Q110 128 220 126 Q330 128 440 70 V130 H0Z" fill="var(--white)"/>
  </svg>
  <div class="abs tagline"><div class="tagline__small">WE'RE IN YOUR</div><div class="tagline__big">NEIGHBOURHOOD!</div></div>
  <svg class="abs" style="left:0;top:0" width="440" height="260" viewBox="0 0 440 260" aria-hidden="true">
    <path class="hang-hole" d="M0 130 H130 Q145 130 155 120 A72 72 0 1 1 155 200 Q145 190 130 190 H0Z"/>
  </svg>
  <div class="abs worker-photo" role="img" aria-label="Photo of a roofer in a blue cap cleaning a gutter"></div>

  <div class="abs slogan">Raised On Care,<br>Proven Through Seasons</div>
  <div class="abs years">32 YEARS IN CALGARY</div>
  <p class="abs offer">We are in your area, contact us today for your Exclusive limited time offer</p>
  <p class="abs fine">*Discounts apply exclusively to new agreements only</p>
  <h2 class="abs estimates">FREE ESTIMATES</h2>
  <div class="abs specialized">SPECIALIZED IN</div>
  <div class="abs spec-item" style="left:35px;top:876px">• Gutters Full<br>&nbsp;&nbsp;&nbsp;Exterior Reno's</div>
  <div class="abs spec-item" style="left:262px;top:876px">• Roofing<br>• Siding</div>
  <div class="abs partners">
    <span class="partner partner--square"></span>
    <span class="partner"></span>
    <span class="partner partner--red"></span>
    <span class="partner partner--round"></span>
    <span class="partner partner--navy"></span>
    <span class="partner partner--green"></span>
  </div>

  <div class="abs band"></div>
  <div class="abs phone-box phone-box--back">(403) 555-0148</div>
  <div class="abs site">www.pellmontshingleworks.com</div>
</section>

</body>
</html>
```